Design a helpdesk ticketing platform *

We are launching a helpdesk ticketing platform. Very much like quellbox.com, merrylark.com, pivolta.com, brisktray.com etc. We have a full mid-fidelity prototype built and we want someone to build the full fidelity of the product.

You can view the full mid-fidelity prototype here: https://lnk.vexora.net/Qa8Lpw

The best way moving forward is to just design the following 4 pages

- Main Dashboard https://lnk.vexora.net/81hRtd
- All tickets https://lnk.vexora.net/jwNoEb
- Viewing a ticket https://lnk.vexora.net/Ys4VmK
- Contacts https://lnk.vexora.net/pHeXuo

Target Market(s)

Small business owners

Industry/Entity Type

Saas

Number of Pages Required

4 page

Font styles to use
Serif
Sans Serif

Colors

Designer to choose colors to be used in the design.

Requirements
Must have
• Must follow the prototype exactly. We are not looking for any UX changes. We want the designe xactly as the prototype is. We are only looking for design ideas.
Should not have
• modern, clean. We'd love to see the primary color as yellow, purple, orange, green or blue. You choose which one you think looks best and go with that.

```html
<!DOCTYPE html>
<html lang="en">
<head>
<meta charset="utf-8">
<title>Deskwell – Dashboard</title>
<link rel="stylesheet" href="https://fonts.googleapis.com/css2?family=Pathway+Gothic+One&family=Open+Sans:wght@400;600&display=swap">
<style>
:root{
  --sidebar:#13c08f;
  --sidebar-active:#0fdca2;
  --sidebar-line:#3fd3a8;
  --page:#f6fce4;
  --topbar:#cfd9d8;
  --row:#ccd8d6;
  --ink:#2d2d2b;
  --ink-soft:#4a4a46;
  --accent:#1fb487;
  --due:#f27a06;
  --overdue:#a5141a;
  --muted:#c4cbca;
  --divider:#e3e8d6;
  --white:#ffffff;
}
*{box-sizing:border-box;margin:0;padding:0}
html,body{width:1200px;height:675px;overflow:hidden}
body{background:var(--page);color:var(--ink);font-family:"Open Sans",sans-serif;position:relative}
.display{font-family:"Pathway Gothic One",sans-serif;text-transform:uppercase}

.sidebar{position:absolute;left:0;top:0;width:244px;height:675px;background:var(--sidebar);color:var(--white)}
.brand{position:absolute;left:37px;top:28px;font-size:33px;letter-spacing:.5px;font-family:"Pathway Gothic One",sans-serif;text-transform:uppercase}
.nav{position:absolute;top:97px;left:0;width:244px;list-style:none}
.nav-item{height:49.5px;display:flex;align-items:center;padding-left:38px;font-size:18px;position:relative}
.nav-item svg{width:19px;height:19px;margin-right:10px;stroke:var(--white);fill:none;stroke-width:1.4}
.nav-item.active{background:var(--sidebar-active)}
.nav-item+.nav-item:not(:nth-child(2))::before{content:"";position:absolute;left:19px;right:19px;top:0;border-top:1px solid var(--sidebar-line)}
.new-ticket{position:absolute;left:27px;top:362px;width:191px;height:36px;background:var(--white);border-radius:4px;color:var(--accent);font-size:16px;display:flex;align-items:center;justify-content:center}

.topbar{position:absolute;left:244px;top:0;width:956px;height:38px;background:var(--topbar);display:flex;align-items:center}
.user{display:flex;align-items:center;margin-left:20px;font-size:12px}
.avatar{width:19px;height:19px;border-radius:50%;background:linear-gradient(#9aa7b0,#6f7c86);border:1.5px solid var(--white);margin-right:10px;flex:none}
.search{margin-left:auto;width:14px;height:14px;margin-right:20px}
.account-link{height:38px;border-left:1px solid #b8c4c3;padding:0 19px 0 18px;display:flex;align-items:center;font-size:12px}

.stats{position:absolute;left:244px;top:38px;width:956px;height:79px;display:flex}
.stat{flex:1;text-align:center;border-right:1px solid var(--divider);padding-top:16px}
.stat:last-child{border-right:none;padding-top:19px}
.stat-label{font-size:12px}
.stat-value{font-size:35px;line-height:1.05}
.stat.due{color:var(--due)}
.stat.overdue{color:var(--overdue)}
.stat.onhold{color:var(--muted)}

.section-title{position:absolute;left:262px;top:146px;font-size:35px}

.activities{position:absolute;left:262px;top:195px;width:920px;list-style:none}
.activity{height:85px;display:flex;padding:16px 0 0 19px}
.activity:nth-child(odd){background:var(--row)}
.ticket-no{width:38px;color:var(--accent);font-size:15px}
.ticket-title{font-size:16px;line-height:1.1}
.ticket-time{font-size:11px;color:var(--ink-soft);margin-top:1px}
.event{display:flex;align-items:center;margin-top:4px;font-size:9.5px;color:var(--ink-soft)}
.event .avatar{width:19px;height:19px;margin-right:6px;background:linear-gradient(#b89a8a,#6e5247)}
.event b{font-weight:600;color:var(--ink);margin-right:3px}
.event b.to{margin-left:3px;margin-right:0}
</style>
</head>
<body>
<aside class="sidebar">
  <div class="brand">Deskwell</div>
  <ul class="nav display">
    <li class="nav-item active"><svg viewBox="0 0 20 20"><circle cx="10" cy="10" r="8.5"/><path d="M10 10l3-4M5 10h1M14 10h1M10 5v1"/></svg>Dashboard</li>
    <li class="nav-item"><svg viewBox="0 0 20 20"><rect x="2" y="5" width="16" height="10" rx="1" transform="rotate(-12 10 10)"/><path d="M6 8h8M6 11h5"/></svg>Tickets</li>
    <li class="nav-item"><svg viewBox="0 0 20 20"><rect x="1.5" y="3.5" width="17" height="13"/><circle cx="7" cy="9" r="2"/><path d="M4 14c1-2.5 5-2.5 6 0M12 8h4M12 11h4"/></svg>Contacts</li>
    <li class="nav-item"><svg viewBox="0 0 20 20"><rect x="1.5" y="3" width="17" height="6" rx="3"/><rect x="1.5" y="11" width="17" height="6" rx="3"/><circle cx="14" cy="6" r="1.5"/><circle cx="6" cy="14" r="1.5"/></svg>Admin settings</li>
    <li class="nav-item"><svg viewBox="0 0 20 20"><rect x="1.5" y="3" width="17" height="6" rx="3"/><rect x="1.5" y="11" width="17" height="6" rx="3"/><circle cx="14" cy="6" r="1.5"/><circle cx="6" cy="14" r="1.5"/></svg>Account &amp; Billing</li>
  </ul>
  <div class="new-ticket display">+ Create a new ticket</div>
</aside>

<header class="topbar display">
  <div class="user"><span class="avatar" role="img" aria-label="Profile photo of Marcus Delley"></span>Marcus Delley</div>
  <svg class="search" viewBox="0 0 14 14" fill="none" stroke="#2d2d2b" stroke-width="1.4"><circle cx="5.5" cy="5.5" r="4.5"/><path d="M9 9l4 4"/></svg>
  <div class="account-link">My Account &amp; Billing</div>
</header>

<section class="stats display">
  <div class="stat"><div class="stat-label">Open tickets</div><div class="stat-value">16</div></div>
  <div class="stat due"><div class="stat-label">Due today</div><div class="stat-value">14</div></div>
  <div class="stat"><div class="stat-label">Unassigned</div><div class="stat-value">14</div></div>
  <div class="stat overdue"><div class="stat-label">Over due</div><div class="stat-value">1</div></div>
  <div class="stat onhold"><div class="stat-label">Onhold</div><div class="stat-value">0</div></div>
  <div class="stat"><div class="stat-label">Not resolved</div><div class="stat-value">11</div></div>
</section>

<h1 class="section-title display">Recent activities</h1>

<ul class="activities">
  <li class="activity">
    <div class="ticket-no display">#15</div>
    <div><div class="ticket-title display">Forgot to CC, trying again</div><div class="ticket-time display">One hour ago</div>
    <div class="event"><span class="avatar" role="img" aria-label="Photo of Priya Holm"></span><b>Priya Holm</b> assigned this ticket to <b class="to">Priya Holm</b></div></div>
  </li>
  <li class="activity">
    <div class="ticket-no display">#15</div>
    <div><div class="ticket-title display">Forgot to CC, trying again</div><div class="ticket-time display">Four hours ago</div>
    <div class="event"><span class="avatar" role="img" aria-label="Photo of Priya Holm"></span><b>Priya Holm</b> assigned this ticket to <b class="to">Priya Holm</b></div></div>
  </li>
  <li class="activity">
    <div class="ticket-no display">#12</div>
    <div><div class="ticket-title display">Test from email</div><div class="ticket-time display">Nine hours ago</div>
    <div class="event"><span class="avatar" role="img" aria-label="Photo of Priya Holm"></span><b>Priya Holm</b> added a note</div></div>
  </li>
  <li class="activity">
    <div class="ticket-no display">#15</div>
    <div><div class="ticket-title display">Test</div><div class="ticket-time display">Yesterday</div>
    <div class="event"><span class="avatar" role="img" aria-label="Photo of Priya Holm"></span><b>Priya Holm</b> assigned this ticket</div></div>
  </li>
  <li class="activity">
    <div class="ticket-no display">#16</div>
    <div><div class="ticket-title display">Test</div><div class="ticket-time display">Yesterday</div>
    <div class="event"><span class="avatar" role="img" aria-label="Photo of Tomas Varga"></span><b>Tomas Varga</b> raised a new ticket</div></div>
  </li>
</ul>
</body>
</html>
```